Window Graphics ‘Opening Soon’ for new Jewellery Boutique

We want to fully cover the shop window for a duration of 6 weeks whilst the refurbishment is going on. The window graphics should be cool, sexy and sophisticated. The graphics should include our company logo ‘THE COPPER LANTERN’ in Gills Sans Font. The shop will be an upmarket jewellery watch shop.

Target Market(s)

Jewellery customers

Industry/Entity Type

Jewellery

Colors

Designer to choose colors to be used in the design.

Requirements
Must have
• Must be loud graphics that catch your attention when walking past. I have provided a graphics example where the colour palette is black, white and shocking pink!
Nice to have
• The Boss is Back…. The Copper Lantern Proudly present a new masterpiece coming soon….

```html
<!DOCTYPE html>
<html lang="en">
<head>
<meta charset="utf-8">
<title>The Copper Lantern – Window Graphics</title>
<link href="https://fonts.googleapis.com/css2?family=Cabin:wght@400;500&display=swap" rel="stylesheet">
<style>
  :root {
    --paper: #ffffff;
    --ink: #ffffff;
    --bronze-dark: #86623f;
    --bronze: #9b7755;
    --bronze-floor: #b48c6b;
    --noir: #19161a;
    --noir-soft: #2a2629;
    --steel: #8f9196;
    --steel-dark: #3b3c41;
    --gold: #f0b65a;
    --gold-deep: #8a4f12;
  }
  * { box-sizing: border-box; margin: 0; padding: 0; }
  html, body {
    width: 903px; height: 1200px; overflow: hidden;
    background: var(--paper);
    font-family: "Cabin", "Gill Sans", sans-serif;
    color: var(--ink);
  }
  .canvas { position: relative; width: 903px; height: 1200px; }

  .window-set { position: absolute; left: 74px; width: 759px; height: 308px; }
  .window-set--bronze { top: 80px; }
  .window-set--steel  { top: 445px; height: 312px; }
  .window-set--noir   { top: 816px; height: 306px; }

  .pane { position: absolute; top: 0; height: 100%; overflow: hidden; }
  .pane--left   { left: 0; width: 132px; }
  .pane--centre { left: 147px; width: 473px; }
  .pane--right  { left: 636px; width: 123px; }

  /* side panel backgrounds */
  .window-set--bronze .pane--left,
  .window-set--bronze .pane--right { background: linear-gradient(90deg, var(--bronze-dark), var(--bronze) 60%, var(--bronze-dark)); }
  .window-set--steel .pane--left  { background: linear-gradient(90deg, var(--noir) 30%, #4a494e); }
  .window-set--steel .pane--right { background: linear-gradient(90deg, #4a494e, var(--noir) 70%); }
  .window-set--noir .pane--left   { background: linear-gradient(90deg, var(--noir) 35%, #4a3325); }
  .window-set--noir .pane--right  { background: linear-gradient(90deg, #4a3325, var(--noir) 65%); }

  /* stage scene areas */
  .stage { position: absolute; inset: 0; }
  .window-set--bronze .stage {
    background:
      radial-gradient(ellipse 60% 18% at 50% 72%, rgba(0,0,0,.25), transparent 70%),
      linear-gradient(180deg, transparent 76%, var(--bronze-floor) 76%, #a67f5f),
      linear-gradient(90deg, var(--bronze) 0 5%, #6e4f34 9%, var(--bronze-dark) 14%, var(--bronze) 50%, var(--bronze-dark) 86%, #6e4f34 91%, var(--bronze) 95%);
  }
  .window-set--steel .stage {
    background:
      radial-gradient(ellipse 60% 18% at 50% 72%, rgba(0,0,0,.3), transparent 70%),
      linear-gradient(180deg, transparent 76%, var(--steel) 76%, var(--steel-dark)),
      linear-gradient(180deg, var(--noir) 30%, #6f7075 70%, transparent 70%),
      linear-gradient(90deg, #8d8e93 0 5%, #2c2c31 9%, #1f1c20 14%, #1f1c20 86%, #2c2c31 91%, #8d8e93 95%);
  }
  .window-set--noir .stage {
    background:
      radial-gradient(ellipse 60% 18% at 50% 72%, rgba(0,0,0,.25), transparent 70%),
      linear-gradient(180deg, transparent 76%, var(--bronze-floor) 76%, #a67f5f),
      linear-gradient(180deg, var(--noir) 30%, #8f6a4a 70%, transparent 70%),
      linear-gradient(90deg, var(--bronze) 0 5%, #4a3325 9%, var(--noir) 14%, var(--noir) 86%, #4a3325 91%, var(--bronze) 95%);
  }

  .platform-curve { position: absolute; left: 0; bottom: 0; width: 100%; height: 80px; }

  .boss-line {
    position: absolute; left: 0; width: 100%; top: 76px;
    text-align: center; font-size: 32px; line-height: 38px; font-weight: 400;
    letter-spacing: 0.5px;
  }

  .headline { position: absolute; left: 0; width: 100%; text-align: center; }
  .brand-name   { top: 48px; font-size: 29px; font-weight: 400; letter-spacing: 0.5px; line-height: 1; }
  .brand-tag    { top: 80px; font-size: 11.5px; font-weight: 400; line-height: 1; }
  .presents     { top: 98px; font-size: 23px; font-weight: 500; line-height: 1; }
  .coming-soon  { top: 188px; font-size: 41px; font-weight: 500; letter-spacing: 1px; line-height: 1; }

  .brand-mark {
    position: absolute; left: 8px; right: 8px; top: 128px;
    text-align: center; font-size: 15px; line-height: 19px; font-weight: 400;
    letter-spacing: 1px;
  }
</style>
</head>
<body>
<main class="canvas">

  <section class="window-set window-set--bronze">
    <div class="pane pane--left">
      <p class="boss-line">THE<br>BOSS<br>IS<br>BAC...</p>
      <svg class="platform-curve" viewBox="0 0 132 80" preserveAspectRatio="none" aria-hidden="true">
        <path d="M132 10 C60 25 30 45 45 80" fill="none" stroke="#c9a37f" stroke-width="2"/>
        <path d="M132 22 C70 35 40 52 60 80" fill="none" stroke="var(--gold)" stroke-width="2"/>
      </svg>
    </div>
    <div class="pane pane--centre">
      <div class="stage" role="img" aria-label="Stage with curtains, round platform, black display bust and cylindrical jewellery stands"></div>
      <h1 class="headline brand-name">THE COPPER LANTERN</h1>
      <p class="headline brand-tag">LUXURY FURNITURE AND INTERIORS</p>
      <p class="headline presents">PROUDLY PRESENT NEW MASTERPIECE</p>
      <p class="headline coming-soon">COMING SOON...</p>
    </div>
    <div class="pane pane--right">
      <p class="brand-mark">THE<br>COPPER<br>LANTERN</p>
      <svg class="platform-curve" viewBox="0 0 123 80" preserveAspectRatio="none" aria-hidden="true">
        <path d="M0 10 C70 25 100 45 80 80" fill="none" stroke="#c9a37f" stroke-width="2"/>
        <path d="M0 22 C60 35 90 52 65 80" fill="none" stroke="var(--gold)" stroke-width="2"/>
      </svg>
    </div>
  </section>

  <section class="window-set window-set--steel">
    <div class="pane pane--left">
      <p class="boss-line">THE<br>BOSS<br>IS<br>BAC...</p>
      <svg class="platform-curve" viewBox="0 0 132 80" preserveAspectRatio="none" aria-hidden="true">
        <path d="M132 10 C60 25 30 45 45 80" fill="none" stroke="#a4a6ab" stroke-width="2"/>
        <path d="M132 22 C70 35 40 52 60 80" fill="none" stroke="var(--gold)" stroke-width="2"/>
      </svg>
    </div>
    <div class="pane pane--centre">
      <div class="stage" role="img" aria-label="Dark stage with grey curtains, round platform, black display bust and cylindrical jewellery stands"></div>
      <h2 class="headline brand-name">THE COPPER LANTERN</h2>
      <p class="headline brand-tag">LUXURY FURNITURE AND INTERIORS</p>
      <p class="headline presents">PROUDLY PRESENT NEW MASTERPIECE</p>
      <p class="headline coming-soon">COMING SOON...</p>
    </div>
    <div class="pane pane--right">
      <p class="brand-mark">THE<br>COPPER<br>LANTERN</p>
      <svg class="platform-curve" viewBox="0 0 123 80" preserveAspectRatio="none" aria-hidden="true">
        <path d="M0 10 C70 25 100 45 80 80" fill="none" stroke="#a4a6ab" stroke-width="2"/>
        <path d="M0 22 C60 35 90 52 65 80" fill="none" stroke="var(--gold)" stroke-width="2"/>
      </svg>
    </div>
  </section>

  <section class="window-set window-set--noir">
    <div class="pane pane--left">
      <p class="boss-line">THE<br>BOSS<br>IS<br>BAC...</p>
      <svg class="platform-curve" viewBox="0 0 132 80" preserveAspectRatio="none" aria-hidden="true">
        <path d="M132 10 C60 25 30 45 45 80" fill="none" stroke="#c9a37f" stroke-width="2"/>
        <path d="M132 22 C70 35 40 52 60 80" fill="none" stroke="var(--gold)" stroke-width="2"/>
      </svg>
    </div>
    <div class="pane pane--centre">
      <div class="stage" role="img" aria-label="Dark stage with bronze curtains, round platform, black display bust and cylindrical jewellery stands"></div>
      <h2 class="headline brand-name">THE COPPER LANTERN</h2>
      <p class="headline brand-tag">LUXURY FURNITURE AND INTERIORS</p>
      <p class="headline presents">PROUDLY PRESENT NEW MASTERPIECE</p>
      <p class="headline coming-soon">COMING SOON...</p>
    </div>
    <div class="pane pane--right">
      <p class="brand-mark">THE<br>COPPER<br>LANTERN</p>
      <svg class="platform-curve" viewBox="0 0 123 80" preserveAspectRatio="none" aria-hidden="true">
        <path d="M0 10 C70 25 100 45 80 80" fill="none" stroke="#c9a37f" stroke-width="2"/>
        <path d="M0 22 C60 35 90 52 65 80" fill="none" stroke="var(--gold)" stroke-width="2"/>
      </svg>
    </div>
  </section>

</main>
</body>
</html>
```